Website re-design

We are a successful furnished apartment provider in Boston. We currently are working on re-designing our website www.ribtenlofts.com to make it more modern, designer look and user friendly. We hired a designer, but are not happy with the designs proposed and want to improve on them. The winning design will be paid regardless of whether we stay with our current designer or not. We want ideas and functional page links to see how it will work. Platform we have chosen is wordpress. Feel free to propose others easy for us to update and modify. We do not like Joomla on which website is currently running. We do not like flash nor long load times.
Please use photos on our website for design presentations. www.ribtenlofts.com

Target Market(s)

doctors, nurses, business men but mostly business women, some post-medical students

Industry/Entity Type

Apartment

Requirements
Must have
• Quick action button for reservation form and a notification and email forwarding system to us of reservation information by potential clients. Blog required with feedback by guests allowed, we can censor which are published. Slide shows of apartments.
Should not have
• No movies.

```html
<!DOCTYPE html>
<html lang="en">
<head>
<meta charset="utf-8">
<title>Ribten Lofts – Furnished Apartments</title>
<link rel="stylesheet" href="https://fonts.googleapis.com/css2?family=Arimo:wght@400;700&family=Marcellus&display=swap">
<style>
:root{
  --black:#000;
  --page:#333333;
  --gold:#d8c089;
  --gold-light:#efe3c0;
  --gold-dark:#8a7433;
  --text:#333;
  --panel:#f4f4f4;
  --white:#fff;
  --dot:#c8c8c8;
}
*{margin:0;padding:0;box-sizing:border-box}
html,body{width:1200px;height:960px;overflow:hidden}
body{background:var(--page);font-family:"Arimo",Arial,sans-serif;color:var(--text);position:relative}
.site-header{position:absolute;left:0;top:0;width:1200px;height:148px;background:var(--black)}
.brand{position:absolute;left:158px;top:30px;display:flex;align-items:center}
.brand-mark{width:57px;height:57px;border-radius:50%;background:var(--gold)}
.brand-text{margin-left:12px}
.brand-name{font-family:"Marcellus",Georgia,serif;font-size:29px;color:var(--gold);letter-spacing:2px;line-height:1}
.brand-tag{font-size:10px;color:var(--gold);letter-spacing:2.6px;margin-top:4px}
.utility{position:absolute;right:161px;top:10px;display:flex;align-items:center;font-size:11px;color:var(--gold);letter-spacing:.5px}
.utility .phone{width:23px;height:23px;background:#a89a78;border-radius:3px;margin-right:9px;display:flex;align-items:center;justify-content:center}
.utility .sep{margin:0 16px}
.utility-rule{position:absolute;left:684px;top:42px;width:355px;height:1px;background:#555}
.social{position:absolute;right:161px;top:53px;display:flex;align-items:center;font-size:11px;color:var(--gold);letter-spacing:.5px}
.badge{width:74px;height:12px;border-radius:6px;background:#8a8060;margin-right:16px}
.share-icon{width:15px;height:15px;background:#b8a97e;margin-right:9px}
.main-nav{position:absolute;top:118px;left:160px;font-size:13px;font-weight:700;color:var(--gold);letter-spacing:1px}
.main-nav span{position:absolute;white-space:nowrap}
.hero{position:absolute;left:158px;top:176px;width:881px;height:234px}
.photo-row{position:absolute;left:0;display:flex;width:881px}
.photo-row.top{top:0;height:95px}
.photo-row.bottom{top:152px;height:82px}
.photo{flex:1;border-right:1px solid #222}
.p1{background:linear-gradient(135deg,#7a5a3c,#c9a77a 60%,#4a3324)}
.p2{background:linear-gradient(135deg,#d9b27a,#f0d7a8 50%,#8b6a42)}
.p3{background:linear-gradient(135deg,#b78c5a,#e6cfa3 50%,#6e5236)}
.p4{background:linear-gradient(135deg,#9aa0a8,#e8e6df 50%,#7a5c3e)}
.p5{background:linear-gradient(135deg,#c9b59a,#efe7da 50%,#8e2a22)}
.p6{background:linear-gradient(135deg,#5a3a22,#a07048 50%,#3a2418)}
.p7{background:linear-gradient(135deg,#d2a66e,#f2dcae 50%,#5a5a6a)}
.p8{background:linear-gradient(135deg,#8e5a36,#b9392c 50%,#4e2e1e)}
.p9{background:linear-gradient(135deg,#c8b8a0,#f4eee4 50%,#9a2a26)}
.p10{background:linear-gradient(135deg,#6a4a20,#c9a044 50%,#2a2a3a)}
.hero-band{position:absolute;left:0;top:95px;width:881px;height:57px;background:linear-gradient(#f2e7c6,#d6c38d);display:flex;align-items:center;justify-content:center;font-size:24px;font-weight:700;color:var(--white);text-shadow:0 1px 3px rgba(80,60,20,.7)}
.intro{position:absolute;left:158px;top:410px;width:881px;height:191px;background:var(--panel)}
.intro p{position:absolute;left:28px;top:48px;width:640px;font-size:22px;line-height:32px;color:var(--text)}
.book-btn{position:absolute;left:676px;top:54px;width:162px;height:56px;border:1px solid #b39c5c;border-radius:3px;background:linear-gradient(#eee2bd,#d2bd84);text-align:center}
.book-btn strong{display:block;font-size:19px;color:var(--white);text-shadow:0 1px 2px rgba(80,60,20,.7);margin-top:8px}
.book-btn small{display:block;font-size:10px;color:#333;margin-top:3px}
.info{position:absolute;left:158px;top:601px;width:881px;height:244px;background:var(--white)}
.info h2{font-size:17px;font-weight:700;color:#333}
.about{position:absolute;left:28px;top:40px;width:160px;font-size:13px;line-height:17px}
.about h2{margin-bottom:10px}
.about a{color:var(--gold-dark);text-decoration:underline}
.newsletter{position:absolute;left:224px;top:40px;width:280px;font-size:13px}
.newsletter h2{margin-bottom:10px}
.email{margin-top:6px;width:262px;height:33px;border:2px solid #bbb;border-radius:4px;padding:8px;color:#aaa;font-size:13px}
.join{margin-top:10px;width:110px;height:30px;border:1px solid #b39c5c;border-radius:3px;background:linear-gradient(#eee2bd,#d2bd84);color:var(--white);font-weight:700;font-size:15px;text-align:center;line-height:28px;text-shadow:0 1px 2px rgba(80,60,20,.7)}
.follow{position:absolute;left:436px;top:145px;display:flex;gap:8px}
.follow span{width:20px;height:20px;border-radius:3px;background:#6a8fc4}
.follow span+span{background:#7cc4e8}
.reviews{position:absolute;left:526px;top:40px;width:335px}
.reviews .badge{position:absolute;left:220px;top:4px;width:112px;background:#ddd}
.review-box{margin-top:12px;width:313px;background:var(--panel);padding:18px 17px;font-size:13px;line-height:17px;color:#111;border-radius:2px}
.review-box cite{display:block;font-style:normal;margin-top:8px;color:#333}
.dots{margin:15px 0 0 128px;display:flex;gap:10px}
.dots span{width:13px;height:13px;border-radius:50%;background:var(--dot)}
.dots span:first-child{background:var(--gold-dark)}
.site-footer{position:absolute;left:155px;top:857px;font-size:10.5px;color:var(--white);letter-spacing:.4px}
</style>
</head>
<body>
<header class="site-header">
  <div class="brand">
    <div class="brand-mark"></div>
    <div class="brand-text">
      <div class="brand-name">RIBTEN LOFTS</div>
      <div class="brand-tag">FURNISHED APARTMENTS</div>
    </div>
  </div>
  <nav class="utility">
    <span class="phone"><svg width="13" height="13" viewBox="0 0 24 24"><path fill="#fff" d="M6.6 10.8a15 15 0 0 0 6.6 6.6l2.2-2.2a1 1 0 0 1 1-.25 11.4 11.4 0 0 0 3.6.6 1 1 0 0 1 1 1V20a1 1 0 0 1-1 1A17 17 0 0 1 3 4a1 1 0 0 1 1-1h3.5a1 1 0 0 1 1 1c0 1.25.2 2.45.6 3.6a1 1 0 0 1-.25 1z"/></svg></span>
    <span>CONTACT RIBTEN LOFTS</span><span class="sep">|</span><span>ABOUT US</span><span class="sep">|</span><span>LINKS</span>
  </nav>
  <div class="utility-rule"></div>
  <div class="social"><span class="badge"></span><span class="share-icon"></span><span>SHARE THIS</span></div>
  <nav class="main-nav">
    <span style="left:0">APARTMENTS</span>
    <span style="left:153px">RATES</span>
    <span style="left:245px">RESERVATIONS</span>
    <span style="left:399px">LOCATION</span>
    <span style="left:516px">BLOG</span>
  </nav>
</header>

<section class="hero">
  <div class="photo-row top">
    <div class="photo p1" role="img" aria-label="Bedroom with bay windows and armchairs"></div>
    <div class="photo p2" role="img" aria-label="Bright studio with windows"></div>
    <div class="photo p3" role="img" aria-label="Living area with fireplace"></div>
    <div class="photo p4" role="img" aria-label="Kitchenette with microwave"></div>
    <div class="photo p5" role="img" aria-label="Sitting room with white armchairs"></div>
  </div>
  <div class="hero-band">Looking for a great apartment? You've found 18 of them.</div>
  <div class="photo-row bottom">
    <div class="photo p6" role="img" aria-label="Lounge with red armchairs"></div>
    <div class="photo p7" role="img" aria-label="Bedroom with grey bedding"></div>
    <div class="photo p8" role="img" aria-label="Living room with red sofa"></div>
    <div class="photo p9" role="img" aria-label="Bedroom with red throw"></div>
    <div class="photo p10" role="img" aria-label="Attic bedroom with patterned bedspread"></div>
  </div>
</section>

<section class="intro">
  <p>Centrally located in Boston’s trendy South End neighborhood,<br>Ribten Lofts furnished apartments are within walking distance<br>to some of Boston’s hottest attraction.</p>
  <a class="book-btn"><strong>Book your stay</strong><small>— pay deposit via PayLink —</small></a>
</section>

<section class="info">
  <div class="about">
    <h2>About us</h2>
    <p>We are operating guest houses for 12 years. Ideal for business and leisure travelers alike,</p>
    <a>Read more</a>
  </div>
  <div class="newsletter">
    <h2>Newsletter</h2>
    <p>Join our E-Mail List&nbsp; and get special offers.</p>
    <div class="email">Your E-Mail</div>
    <div class="join">Join now</div>
  </div>
  <div class="follow"><span></span><span></span></div>
  <div class="reviews">
    <h2>What others are saying</h2>
    <span class="badge"></span>
    <blockquote class="review-box">Good central location in lively neighbour-<br>hood - Nice owner - Free wifi - Comfortable<br>No noise<cite>— Mark T</cite></blockquote>
    <div class="dots"><span></span><span></span><span></span><span></span></div>
  </div>
</section>

<footer class="site-footer">© Ribten Lofts 2010 - All Rights Reserved</footer>
</body>
</html>
```